Video Learning Web Application Site Design

We are a new company that produce and distribute educational videos using a subscription model on our website. The videos are streamed on our website and users can tailor their own course packages by creating playlists. Each video-lesson are also split into several smaller segments, and it should be easy to find and play those segments.

Please note that both the screenshots and wireframes provided are only how it looks right now, if you as the designer have a better idea on how to present it then please share it.
Updates

Please view the screenshots as well, I believe I forgot to include two buttons on the wireframes that should be on the Our Courses page. Also, there is no need to make a carbon copy of the wireframes/screenshots, I'd like you designers to come up with a better way of displaying the information if possible. For inspiration you can look at sites like ClipNest (I like the simplicity of their design) and to some extent the Prism UI where they divide different areas of the page into clear "zones".

Thanks,

Reason: I have to extend the deadline because I've been really ill the last week. Will go through the current submissions now and provide feedback and looking forward to more submissions.

Target Market(s)

College and University students. Professionals wanting to expand their knowledge and people that want to learn new skills to get a promotion/new job.

Industry/Entity Type

Tailor

Requirements
Must have
• Must include the logo from the file "brightleaf-logo".
• Should include two pages, one of the video-player page and one of the course list.
• Try to incorporate the colors from the logo.
• Please note: If you look at the video-player.png file just below "Starte Tavla, bruke..." there are two rows, those are sub-parts of the lesson. Both these and the main lesson itself must have some easy way to Play and Add to Playlist.
Nice to have
• We prefer flat design, with simple and clean icons. Don't overdo the colors, stay within 3-4 colors with variations of them.
Should not have
• 3D-like elements, lot of shadows or hard to ready text.

```html
<!DOCTYPE html>
<html lang="en">
<head>
<meta charset="utf-8">
<title>Brightleaf – Your Courses</title>
<link href="https://fonts.googleapis.com/css2?family=Source+Sans+3:wght@400;600;700&display=swap" rel="stylesheet">
<style>
:root{
  --brand:#0a7aa6;
  --brand-dark:#066790;
  --brand-deep:#0c4a66;
  --link:#1279a8;
  --accent:#e07a1e;
  --accent-soft:#f5b15a;
  --remove:#e0682a;
  --ink:#333;
  --muted:#777;
  --line:#dcdcdc;
  --panel:#ececec;
  --footer:#333;
}
*{box-sizing:border-box;margin:0;padding:0}
html,body{width:1200px;height:801px;overflow:hidden;background:#fff}
body{font-family:"Source Sans 3",Arial,sans-serif;color:var(--ink)}
.page{position:relative;width:1150px;height:768px;transform:scale(1.0435);transform-origin:0 0}
.abs{position:absolute}

/* header */
.site-header{position:absolute;left:0;top:0;width:1150px;height:88px;background:linear-gradient(#fafafa,#efefef);border-bottom:3px solid var(--brand)}
.brand{position:absolute;left:68px;top:16px;display:flex;align-items:center;gap:10px}
.brand-dot{width:46px;height:46px;border-radius:50%;background:var(--brand)}
.brand-name{font-size:40px;font-weight:700;color:var(--brand);line-height:1}
.search{position:absolute;left:444px;top:22px;width:263px;height:36px;background:#fff;border:1px solid #d6d6d6;border-radius:2px}
.search span{position:absolute;left:18px;top:8px;font-size:14px;color:#999}
.search-btn{position:absolute;right:5px;top:5px;width:25px;height:23px;background:#8a8a8a;border-radius:2px}
.account{position:absolute;left:816px;top:26px;font-size:15px;color:var(--ink)}
.account .sep{margin:0 10px}

/* sidebar */
.sidebar{position:absolute;left:63px;top:88px;width:245px;height:624px;background:linear-gradient(var(--brand-dark),var(--brand) 30%,#087aa8)}
.nav-group{padding:25px 0 13px 0;border-bottom:1px solid rgba(255,255,255,.18);position:relative}
.nav-title{display:flex;align-items:center;color:#fff;font-size:17px;font-weight:600;padding-left:20px}
.nav-title .chev{font-size:14px;width:21px}
.nav-links{list-style:none;padding-left:41px;margin-top:6px}
.nav-links li{font-size:14px;color:#cfe6f1;line-height:22px}
.nav-links li.active{color:var(--accent-soft)}
.add-playlist{position:absolute;right:20px;top:25px}

/* main */
.page-title{position:absolute;left:334px;top:95px;font-size:24px;font-weight:600;color:var(--brand-deep)}
.course-card{position:absolute;left:335px;top:140px;width:740px;height:260px;border:1px solid var(--line);background:linear-gradient(#fff 65%,#f1f1f1)}
.video-frame{position:absolute;left:5px;top:5px;width:349px;height:206px;border:1px solid var(--line);background:#eee;padding:5px}
.video-still{width:337px;height:193px;background:linear-gradient(135deg,#6e6a66,#4a4644 60%,#8a8580)}
.play{position:absolute;left:139px;top:67px}
.course-name{position:absolute;left:13px;top:226px;font-size:14.5px;color:var(--link)}
.remove{position:absolute;left:231px;top:228px;font-size:12.5px;color:var(--remove);display:flex;align-items:center;gap:6px}
.segment-title{position:absolute;left:382px;top:20px;font-size:16px;color:var(--accent)}
.col-head{font-size:14px;font-weight:600;color:var(--ink)}
.cues{position:absolute;left:383px;top:53px}
.cue-list{list-style:none;margin-top:8px;width:128px;height:122px;background:var(--panel);border:1px solid #d6d6d6;padding:10px 0 0 18px}
.cue-list li{font-size:13px;color:#555;line-height:26px}
.files{position:absolute;left:533px;top:53px}
.file-list{list-style:none;margin-top:8px}
.file-list li{font-size:12.5px;color:var(--ink);line-height:26px}
.dq{color:#666;margin-right:4px}

.show-cues{position:absolute;left:335px;top:414px;width:106px;height:36px;border:1px solid #ccc;background:#fff;font:14px "Source Sans 3",Arial,sans-serif;color:var(--link)}

.cue-tree{position:absolute;left:337px;top:474px;display:flex}
.tree-col{width:197px;list-style:none}
.tree-item{display:flex;align-items:center;height:20px;font-size:14px;color:var(--link)}
.tree-child{display:flex;align-items:center;height:30px;padding-left:49px;font-size:14px;color:#888}
.tree-child:first-of-type{margin-top:3px}
.ch{color:#666;width:18px;font-size:13px}
.star{color:#777;width:18px;font-size:14px}
.tri{margin:0 6px 0 11px}

/* footer */
.site-footer{position:absolute;left:0;top:720px;width:1150px;height:48px;background:linear-gradient(#444,#222)}
.copyright{position:absolute;left:65px;top:16px;font-size:13.5px;color:#cfcfcf}
.social{position:absolute;left:1028px;top:12px;display:flex;gap:9px}
.social span{width:24px;height:24px;border-radius:50%;background:#6a6a6a}
</style>
</head>
<body>
<div class="page">
  <header class="site-header">
    <div class="brand"><span class="brand-dot"></span><span class="brand-name">brightleaf</span></div>
    <div class="search"><span>Search</span>
      <div class="search-btn"><svg width="25" height="23" viewBox="0 0 25 23"><circle cx="11" cy="10" r="5" fill="none" stroke="#fff" stroke-width="2"/><line x1="15" y1="14" x2="19" y2="18" stroke="#fff" stroke-width="2.5"/></svg></div>
    </div>
    <div class="account">Logged in john@brightleaf-mail.net<span class="sep">|</span>Log out</div>
  </header>

  <nav class="sidebar">
    <div class="nav-group">
      <div class="nav-title"><span class="chev">››</span>Introduction</div>
      <ul class="nav-links"><li class="active">Introduction</li></ul>
    </div>
    <div class="nav-group">
      <div class="nav-title"><span class="chev">››</span>Modules</div>
      <ul class="nav-links"><li>Our Courses</li><li>Your Courses</li></ul>
    </div>
    <div class="nav-group" style="padding-bottom:22px">
      <div class="nav-title"><span class="chev">››</span>Playlists</div>
      <svg class="add-playlist" width="14" height="14" viewBox="0 0 14 14"><circle cx="7" cy="7" r="7" fill="#fff"/><path d="M7 3.5v7M3.5 7h7" stroke="var(--brand)" stroke-width="2"/></svg>
    </div>
  </nav>

  <h1 class="page-title">Your Courses</h1>

  <section class="course-card">
    <div class="video-frame">
      <div class="video-still" role="img" aria-label="Lesson video still: a student working at a laptop"></div>
      <svg class="play" width="72" height="72" viewBox="0 0 72 72"><circle cx="36" cy="36" r="33" fill="none" stroke="#fff" stroke-width="5"/><path d="M28 22v28l22-14z" fill="#fff"/></svg>
    </div>
    <div class="course-name">Tavla 2013 &nbsp;-&nbsp; Beginner</div>
    <div class="remove"><svg width="11" height="11" viewBox="0 0 11 11"><path d="M1.5 1.5l8 8M9.5 1.5l-8 8" stroke="var(--remove)" stroke-width="2.4"/></svg>Remove this course</div>
    <div class="segment-title">Item 1</div>
    <div class="cues">
      <div class="col-head">Cues</div>
      <ul class="cue-list"><li><span class="dq">»</span>Child 1</li><li><span class="dq">»</span>Child 2</li><li><span class="dq">»</span>Child 3</li><li><span class="dq">»</span>Child 4</li></ul>
    </div>
    <div class="files">
      <div class="col-head">Files</div>
      <ul class="file-list"><li><span class="dq">»</span>Download Lesson file(xls)</li><li><span class="dq">»</span>Download Study material (doc)</li></ul>
    </div>
  </section>

  <button class="show-cues">Show all cues</button>

  <div class="cue-tree">
    <ul class="tree-col">
      <li class="tree-item"><span class="ch">››</span><span class="star">★</span><svg class="tri" width="10" height="7"><path d="M0 0h10L5 7z" fill="var(--link)"/></svg>Item 1</li>
      <li class="tree-child"><span class="ch">››</span><span class="star">★</span>Child 1</li>
      <li class="tree-child"><span class="ch">››</span><span class="star">★</span>Child 2</li>
      <li class="tree-child"><span class="ch">››</span><span class="star">★</span>Child 3</li>
      <li class="tree-child"><span class="ch">››</span><span class="star">★</span>Child 4</li>
    </ul>
    <ul class="tree-col">
      <li class="tree-item"><span class="ch">››</span><span class="star">★</span><svg class="tri" width="10" height="7"><path d="M0 0h10L5 7z" fill="var(--link)"/></svg>Item 2</li>
      <li class="tree-child"><span class="ch">››</span><span class="star">★</span>Child 5</li>
      <li class="tree-child"><span class="ch">››</span><span class="star">★</span>Child 6</li>
      <li class="tree-child"><span class="ch">››</span><span class="star">★</span>Child 7</li>
      <li class="tree-child"><span class="ch">››</span><span class="star">★</span>Child 8</li>
    </ul>
    <ul class="tree-col">
      <li class="tree-item"><span class="ch">››</span><span class="star">★</span><svg class="tri" width="10" height="7"><path d="M0 0h10L5 7z" fill="var(--link)"/></svg>Item 3</li>
      <li class="tree-child"><span class="ch">››</span><span class="star">★</span>Child 9</li>
      <li class="tree-child"><span class="ch">››</span><span class="star">★</span>Child 10</li>
      <li class="tree-child"><span class="ch">››</span><span class="star">★</span>Child 11</li>
      <li class="tree-child"><span class="ch">››</span><span class="star">★</span>Child 12</li>
    </ul>
    <ul class="tree-col">
      <li class="tree-item"><span class="ch">››</span><span class="star">★</span><svg class="tri" width="10" height="7"><path d="M0 0h10L5 7z" fill="var(--link)"/></svg>Item 4</li>
      <li class="tree-child"><span class="ch">››</span><span class="star">★</span>Child 13</li>
      <li class="tree-child"><span class="ch">››</span><span class="star">★</span>Child 14</li>
      <li class="tree-child"><span class="ch">››</span><span class="star">★</span>Child 15</li>
      <li class="tree-child"><span class="ch">››</span><span class="star">★</span>Child 16</li>
    </ul>
  </div>

  <footer class="site-footer">
    <div class="copyright">Copyright &nbsp;© &nbsp;2013 &nbsp;Brightleaf. &nbsp;All rights reserved</div>
    <div class="social"><span></span><span></span></div>
  </footer>
</div>
</body>
</html>
```